IG ad to attract older men for better health #1

I want a bold headline Photofeed Ad that coordinate with my website design with a racy sexy woman to attract men 45yrs old plus. See Two samples attached

Target Market(s)

Men 45 years old and older

Industry/Entity Type

Health And Wellness

Requirements
Must have
• eye catching appeal to men
Nice to have
• The copy to read
Kestrel61go is the headline at the top of the page. Then the copy reads...
"I want to seduce you to better health with a little T&A. Remove the excuses, provide ridiculously simple tips and advice to get you started on a path of lasting heath." Want more?

```html
<!DOCTYPE html>
<html lang="en">
<head>
<meta charset="utf-8">
<title>Kestrel61go – Health Ad Set</title>
<link rel="stylesheet" href="https://fonts.googleapis.com/css2?family=Montserrat:ital,wght@0,400;0,500;0,600;0,700;0,800;1,700&family=Open+Sans:wght@400&display=swap">
<style>
  :root {
    --page: #ffffff;
    --ui-ink: #262626;
    --ui-muted: #8e8e8e;
    --ui-line: #cfcfcf;
    --ui-link: #1c3f8f;
    --alert: #ef4457;
    --avatar: #f0615a;
    --ink-dark: #0c0a0a;
    --peach: #f7b58a;
    --apricot: #e9a068;
    --wine: #4e0e08;
    --wine-deep: #3a0904;
    --wine-shadow: #2a0806;
    --umber: #2e1508;
    --umber-deep: #3a1a0c;
    --cta-ink: #3a0a02;
  }
  * { box-sizing: border-box; margin: 0; padding: 0; }
  html, body { width: 1200px; height: 941px; overflow: hidden; background: var(--page); }
  body { font-family: "Montserrat", sans-serif; position: relative; color: var(--ui-ink); }

  .icon-sprite { position: absolute; width: 0; height: 0; overflow: hidden; }
  .icon { position: absolute; width: 27px; height: 27px; fill: none; stroke: var(--ui-ink); stroke-width: 1.8; stroke-linecap: round; stroke-linejoin: round; }

  /* phone feed frame */
  .phone {
    position: absolute;
    top: 88px;
    width: 455px;
    height: 786px;
    background: var(--page);
    box-shadow: 3px 3px 4px rgba(0,0,0,0.22);
  }
  .phone--left { left: 79px; }
  .phone--right { left: 666px; }

  .app-bar { position: absolute; top: 0; left: 0; width: 100%; height: 54px; border-bottom: 1px solid var(--ui-line); }
  .app-bar .icon--camera { left: 14px; top: 12px; width: 32px; height: 32px; }
  .app-name {
    position: absolute; left: 0; right: 0; top: 12px;
    text-align: center; font-weight: 600; font-size: 24px; color: var(--ui-ink);
  }
  .badge {
    position: absolute; left: 411px; top: 14px; width: 28px; height: 28px; border-radius: 50%;
    background: var(--alert); color: #fff; font-size: 14px; font-weight: 500;
    display: flex; align-items: center; justify-content: center;
  }

  .post-head { position: absolute; top: 54px; left: 0; width: 100%; height: 58px; }
  .avatar {
    position: absolute; left: 87px; top: 4px; width: 46px; height: 46px;
    left: 9px; border-radius: 50%; background: var(--avatar);
  }
  .avatar svg { position: absolute; left: 11px; top: 10px; width: 24px; height: 24px; fill: none; stroke: #fff; stroke-width: 2; }
  .post-head .handle { position: absolute; left: 66px; top: 17px; font-size: 16.5px; font-weight: 500; }
  .post-head .more-dots { position: absolute; left: 418px; top: 25px; width: 18px; height: 5px; }

  .post-actions { position: absolute; top: 583px; left: 0; width: 100%; height: 30px; }
  .post-actions .icon--like { left: 35px; fill: var(--alert); stroke: var(--alert); }
  .post-actions .icon--comment { left: 84px; }
  .post-actions .icon--send { left: 132px; }
  .post-actions .icon--save { left: 414px; }

  .post-meta { position: absolute; left: 35px; top: 624px; font-size: 15.5px; }
  .post-caption { position: absolute; left: 35px; top: 643px; font-size: 16.5px; white-space: nowrap; }
  .post-caption b { font-weight: 700; margin-right: 4px; }
  .post-caption .mention { color: var(--ui-link); }
  .post-caption .more { color: var(--ui-muted); font-size: 14px; }
  .post-comments { position: absolute; left: 35px; top: 673px; font-family: "Open Sans", sans-serif; font-size: 14px; color: var(--ui-muted); }
  .add-comment { position: absolute; left: 33px; top: 698px; width: 30px; height: 30px; border-radius: 50%; background: #9a9a9a; }
  .add-comment-label { position: absolute; left: 75px; top: 704px; font-family: "Open Sans", sans-serif; font-size: 14px; color: var(--ui-muted); }

  .tab-bar { position: absolute; left: 0; top: 730px; width: 100%; height: 56px; border-top: 1px solid var(--ui-line); }
  .tab-bar .icon { top: 14px; }
  .tab-bar .icon--home { left: 33px; fill: var(--ui-ink); }
  .tab-bar .icon--search { left: 123px; }
  .tab-bar .icon--add { left: 215px; }
  .tab-bar .icon--activity { left: 305px; }
  .tab-bar .icon--profile { left: 397px; }
  .tab-bar .active-dot { position: absolute; left: 44px; top: 46px; width: 5px; height: 5px; border-radius: 50%; background: var(--alert); }

  /* ad artwork, built at 560 and fitted to the feed */
  .ad {
    position: absolute;
    left: -1px;
    top: 112px;
    width: 560px;
    height: 560px;
    background: var(--ink-dark);
    overflow: hidden;
    transform: scale(0.8143);
    transform-origin: 0 0;
  }
  .ad__photo { position: absolute; top: 0; left: 0; height: 100%; }
  .ad--back .ad__photo {
    width: 330px;
    background: radial-gradient(ellipse 45% 60% at 50% 55%, #c98a6a 0%, #8a5038 40%, #2a1410 75%, var(--ink-dark) 100%);
  }
  .ad--front .ad__photo {
    width: 300px;
    background: radial-gradient(ellipse 45% 65% at 45% 55%, #c88e70 0%, #7a4a35 40%, #24140e 75%, var(--ink-dark) 100%);
  }
  .shape { position: absolute; }

  .headline {
    position: absolute;
    top: 28px;
    right: 32px;
    font-weight: 800;
    font-size: 48px;
    line-height: 1;
    letter-spacing: -0.5px;
    white-space: nowrap;
  }
  .ad--back .headline { color: var(--peach); }
  .ad--front .headline { color: var(--apricot); right: 34px; }

  .quote-box { position: absolute; }
  .ad--back .quote-box {
    left: 282px; top: 164px; width: 261px; height: 236px;
    background: linear-gradient(180deg, var(--wine) 0%, var(--wine-deep) 100%);
  }
  .ad--front .quote-box {
    left: 279px; top: 156px; width: 281px; height: 267px;
    background: var(--umber-deep);
  }
  .quote-box p {
    position: absolute;
    top: 36px;
    text-align: right;
    white-space: nowrap;
    font-weight: 600;
    font-size: 17px;
    line-height: 22.2px;
  }
  .ad--back .quote-box p { color: var(--peach); right: 17px; }
  .ad--front .quote-box p { color: var(--apricot); right: 36px; top: 44px; }

  .cta {
    position: absolute;
    display: flex;
    align-items: center;
    justify-content: center;
    font-size: 21.5px;
    color: var(--cta-ink);
  }
  .ad--back .cta {
    left: 381px; top: 491px; width: 162px; height: 34px;
    background: var(--peach); font-weight: 700;
  }
  .ad--front .cta {
    left: 353px; top: 490px; width: 188px; height: 33px;
    font-weight: 700; font-style: italic;
  }
  .ad--front .cta svg { position: absolute; inset: 0; }
  .ad--front .cta span { position: relative; }
</style>
</head>
<body>

<svg class="icon-sprite" aria-hidden="true">
  <defs>
    <symbol id="i-camera" viewBox="0 0 24 24"><rect x="2" y="6" width="20" height="15" rx="3"/><path d="M8 6l1.6-2.6h4.8L16 6"/><circle cx="12" cy="13.5" r="4"/></symbol>
    <symbol id="i-heart" viewBox="0 0 24 24"><path d="M12 20.5s-8.5-5.2-8.5-11A4.6 4.6 0 0 1 12 7a4.6 4.6 0 0 1 8.5 2.5c0 5.8-8.5 11-8.5 11z"/></symbol>
    <symbol id="i-comment" viewBox="0 0 24 24"><path d="M20.5 12a8.5 8.5 0 1 0-3.1 6.6L21 20.5l-.9-3.9A8.5 8.5 0 0 0 20.5 12z"/></symbol>
    <symbol id="i-send" viewBox="0 0 24 24"><path d="M2.5 3.5h19L12.5 21l-2-9z"/><path d="M10.5 12l11-8.5"/></symbol>
    <symbol id="i-save" viewBox="0 0 24 24"><path d="M5 2.5h14v19l-7-6-7 6z"/></symbol>
    <symbol id="i-home" viewBox="0 0 24 24"><path d="M3 11l9-8 9 8v10h-6v-5.5h-6V21H3z"/></symbol>
    <symbol id="i-search" viewBox="0 0 24 24"><circle cx="10.5" cy="10.5" r="7.5"/><path d="M16 16l5.5 5.5"/></symbol>
    <symbol id="i-add" viewBox="0 0 24 24"><rect x="2.5" y="2.5" width="19" height="19" rx="2.5"/><path d="M12 7.5v9M7.5 12h9"/></symbol>
    <symbol id="i-user" viewBox="0 0 24 24"><circle cx="12" cy="7.5" r="4.5"/><path d="M3 21.5c.8-4.7 4.6-7 9-7s8.2 2.3 9 7"/></symbol>
  </defs>
</svg>

<!-- Left feed post -->
<article class="phone phone--left">
  <header class="app-bar">
    <svg class="icon icon--camera"><use href="#i-camera"/></svg>
    <div class="app-name">Photofeed</div>
    <div class="badge">16</div>
  </header>
  <div class="post-head">
    <div class="avatar"><svg viewBox="0 0 24 24"><use href="#i-user"/></svg></div>
    <span class="handle">jhon_doe</span>
    <svg class="more-dots" viewBox="0 0 18 5"><circle cx="2.5" cy="2.5" r="2" fill="#262626"/><circle cx="9" cy="2.5" r="2" fill="#262626"/><circle cx="15.5" cy="2.5" r="2" fill="#262626"/></svg>
  </div>

  <section class="ad ad--back">
    <div class="ad__photo" role="img" aria-label="Photo of a red-haired woman in black lingerie seen from behind against a dark backdrop"></div>
    <div class="shape" style="left:18px;top:0;width:22px;height:67px;background:var(--peach)"></div>
    <div class="shape" style="left:495px;top:143px;width:65px;height:21px;background:var(--peach)"></div>
    <div class="shape" style="left:0;top:385px;width:34px;height:21px;background:var(--wine)"></div>
    <div class="shape" style="left:318px;top:400px;width:225px;height:21px;background:var(--wine-shadow)"></div>
    <div class="shape" style="left:505px;top:454px;width:21px;height:106px;background:var(--wine)"></div>
    <h1 class="headline">Kestrel61go</h1>
    <div class="quote-box">
      <p>"I want to seduce you<br>to better health with a<br>little T&amp;A. Remove the<br>excuses, provide<br>ridiculously simple tips<br>and advice to get you<br>started on a path of<br>lasting health."</p>
    </div>
    <div class="cta">Want more?</div>
  </section>

  <div class="post-actions">
    <svg class="icon icon--like"><use href="#i-heart"/></svg>
    <svg class="icon icon--comment"><use href="#i-comment"/></svg>
    <svg class="icon icon--send"><use href="#i-send"/></svg>
    <svg class="icon icon--save"><use href="#i-save"/></svg>
  </div>
  <p class="post-meta">1,989 likes</p>
  <p class="post-caption"><b>jhon_doe</b> Lorem ipsum dolor <span class="mention">@your_name...</span><span class="more">more</span></p>
  <p class="post-comments">View all 99 comments</p>
  <div class="add-comment"></div>
  <p class="add-comment-label">Add a comment...</p>
  <nav class="tab-bar">
    <svg class="icon icon--home"><use href="#i-home"/></svg>
    <svg class="icon icon--search"><use href="#i-search"/></svg>
    <svg class="icon icon--add"><use href="#i-add"/></svg>
    <svg class="icon icon--activity"><use href="#i-heart"/></svg>
    <svg class="icon icon--profile"><use href="#i-user"/></svg>
    <span class="active-dot"></span>
  </nav>
</article>

<!-- Right feed post -->
<article class="phone phone--right">
  <header class="app-bar">
    <svg class="icon icon--camera"><use href="#i-camera"/></svg>
    <div class="app-name">Photofeed</div>
    <div class="badge">16</div>
  </header>
  <div class="post-head">
    <div class="avatar"><svg viewBox="0 0 24 24"><use href="#i-user"/></svg></div>
    <span class="handle">jhon_doe</span>
    <svg class="more-dots" viewBox="0 0 18 5"><circle cx="2.5" cy="2.5" r="2" fill="#262626"/><circle cx="9" cy="2.5" r="2" fill="#262626"/><circle cx="15.5" cy="2.5" r="2" fill="#262626"/></svg>
  </div>

  <section class="ad ad--front">
    <div class="ad__photo" role="img" aria-label="Photo of a dark-haired woman in black lace lingerie posing against a dark backdrop"></div>
    <div class="shape" style="left:34px;top:10px;width:34px;height:34px;background:var(--apricot)"></div>
    <div class="shape" style="left:506px;top:92px;width:35px;height:35px;border:5px solid var(--umber)"></div>
    <div class="shape" style="left:0;top:392px;width:34px;height:34px;background:var(--umber)"></div>
    <h1 class="headline">Kestrel61go</h1>
    <div class="quote-box">
      <p>"I want to seduce you to<br>better health with a<br>little T&amp;A. Remove the<br>excuses, provide<br>ridiculously simple tips<br>and advice to get you<br>started on a path of<br>lasting health."</p>
    </div>
    <div class="shape" style="left:321px;top:404px;width:35px;height:35px;border:4px solid var(--apricot)"></div>
    <div class="cta">
      <svg width="188" height="33" viewBox="0 0 188 33" aria-hidden="true"><polygon points="18,0 188,0 171,33 0,33" fill="#e9a068"/></svg>
      <span>Want more?</span>
    </div>
  </section>

  <div class="post-actions">
    <svg class="icon icon--like"><use href="#i-heart"/></svg>
    <svg class="icon icon--comment"><use href="#i-comment"/></svg>
    <svg class="icon icon--send"><use href="#i-send"/></svg>
    <svg class="icon icon--save"><use href="#i-save"/></svg>
  </div>
  <p class="post-meta">1,989 likes</p>
  <p class="post-caption"><b>jhon_doe</b> Lorem ipsum dolor <span class="mention">@your_name...</span><span class="more">more</span></p>
  <p class="post-comments">View all 99 comments</p>
  <div class="add-comment"></div>
  <p class="add-comment-label">Add a comment...</p>
  <nav class="tab-bar">
    <svg class="icon icon--home"><use href="#i-home"/></svg>
    <svg class="icon icon--search"><use href="#i-search"/></svg>
    <svg class="icon icon--add"><use href="#i-add"/></svg>
    <svg class="icon icon--activity"><use href="#i-heart"/></svg>
    <svg class="icon icon--profile"><use href="#i-user"/></svg>
    <span class="active-dot"></span>
  </nav>
</article>

</body>
</html>
```